Small Business Consulting Firm Needs Business Card Design

Need a sleek modern business card with 2 sides matching the colors of our logo. We will be placing these with a mailer we are sending out. These business cards will only ever be given to business owners. We operate helping businesses who are struggling with cash flow or finances. If the green and blue design needs to be moved to the right of "Harborline Crest Consulting" for aesthetic purposes that is ok. We will need an editable file if possible. We would like to include the reps name, email, website, and phone number. For now just use Peter Vance, pvance@harborlinecrest.com, www.harborlinecrest.com, and 833-555-0172.

```html
<!DOCTYPE html>
<html lang="en">
<head>
<meta charset="utf-8">
<title>Harborline Crest Consulting — Business Card</title>
<link href="https://fonts.googleapis.com/css2?family=Source+Sans+3:wght@400;500&display=swap" rel="stylesheet">
<style>
  :root {
    --backdrop: #d8d3ca;
    --card: #f1f1ef;
    --ink: #4a4a4a;
    --ink-soft: #555555;
    --blue: #1a86cf;
    --green: #6cb33f;
    --rule: #8c8c8c;
  }
  * { margin: 0; padding: 0; box-sizing: border-box; }
  html, body {
    width: 900px; height: 1200px; overflow: hidden;
    background: var(--backdrop);
    font-family: "Source Sans 3", "Helvetica Neue", Arial, sans-serif;
    color: var(--ink);
  }
  .canvas { position: relative; width: 900px; height: 1200px; }
  .card {
    position: absolute; left: 77px; width: 747px; height: 437px;
    background: var(--card);
    box-shadow: 0 2px 6px rgba(0,0,0,0.25);
  }
  .card--front { top: 134px; }
  .card--back { top: 638px; }

  /* Front */
  .front-brand {
    position: absolute; left: 0; right: 0; top: 124px;
    display: flex; flex-direction: column; align-items: center;
  }
  .brand-square { width: 70px; height: 70px; background: var(--green); margin-bottom: 36px; }
  .brand-name {
    font-size: 28px; font-weight: 400; letter-spacing: 1.5px;
    text-transform: uppercase; color: var(--ink); line-height: 1;
  }
  .brand-tag {
    margin-top: 8px; padding-left: 62px;
    font-size: 13px; font-weight: 400; letter-spacing: 6px;
    text-transform: uppercase; color: var(--ink);
  }
  .front-web {
    position: absolute; left: 0; right: 0; top: 388px; text-align: center;
    font-size: 17px; letter-spacing: 3px; color: var(--ink);
  }
  .front-web .accent { color: var(--green); }

  /* Back */
  .back-brand {
    position: absolute; left: 150px; top: 168px; width: 160px;
    display: flex; flex-direction: column; align-items: flex-start;
  }
  .back-brand .brand-square { width: 52px; height: 52px; margin-bottom: 18px; }
  .back-brand .brand-name { font-size: 17px; letter-spacing: 1px; line-height: 1.3; }
  .divider {
    position: absolute; left: 368px; top: 154px; width: 1px; height: 140px;
    background: var(--rule);
  }
  .rep { position: absolute; left: 431px; top: 150px; }
  .rep-name { font-size: 29px; font-weight: 400; line-height: 1; }
  .rep-name .first { color: var(--blue); }
  .rep-name .last { color: var(--green); }
  .rep-title { margin-top: 4px; font-size: 17px; color: var(--ink-soft); }
  .contact-list { list-style: none; margin-top: 24px; }
  .contact-list li {
    display: flex; align-items: center; height: 22px;
    font-size: 17px; color: var(--ink-soft);
  }
  .contact-list svg { width: 13px; height: 13px; margin-right: 15px; fill: var(--blue); flex: none; }
</style>
</head>
<body>
<div class="canvas">

  <section class="card card--front">
    <div class="front-brand">
      <div class="brand-square"></div>
      <div class="brand-name">Harborline Crest</div>
      <div class="brand-tag">Consulting</div>
    </div>
    <div class="front-web">www.<span class="accent">harborlinecres</span>t.com</div>
  </section>

  <section class="card card--back">
    <div class="back-brand">
      <div class="brand-square"></div>
      <div class="brand-name">HARBORLINE CREST CONSULTING</div>
    </div>
    <div class="divider"></div>
    <div class="rep">
      <div class="rep-name"><span class="first">Peter</span> <span class="last">Vance</span></div>
      <div class="rep-title">CEO/ Founder</div>
      <ul class="contact-list">
        <li>
          <svg viewBox="0 0 16 16" aria-hidden="true"><path d="M3.5 1l2.5 3-1.5 2c1 2 2.5 3.5 4.5 4.5l2-1.5 3 2.5-1.5 2.5C7 15 1 9 1 2.5z"/></svg>
          833-555-0172
        </li>
        <li>
          <svg viewBox="0 0 16 16" aria-hidden="true"><circle cx="8" cy="8" r="7"/><path d="M1 8h14M8 1c-3 3.5-3 10.5 0 14M8 1c3 3.5 3 10.5 0 14" stroke="#f1f1ef" stroke-width="1.2" fill="none"/></svg>
          pvance@harborlinecrest.com
        </li>
        <li>
          <svg viewBox="0 0 16 16" aria-hidden="true"><rect x="1" y="3" width="14" height="10"/><path d="M1 3l7 6 7-6" stroke="#f1f1ef" stroke-width="1.2" fill="none"/></svg>
          www.harborlinecrest.com
        </li>
      </ul>
    </div>
  </section>

</div>
</body>
</html>
```